Copperline Ridge Management

I need a professional website. My current website is copperlineridgemanagement.com and I hate it. It was created with some AI tool very quickly because I needed a site up and running with no advanced notice. I’m open to all designs .. I trust you, the professionals will deliver the results I’m anxiously awaiting! :)

```html
<!DOCTYPE html>
<html lang="en">
<head>
<meta charset="utf-8">
<title>Copperline Ridge Management</title>
<link href="https://fonts.googleapis.com/css2?family=Poppins:ital,wght@0,400;0,500;0,600;0,700;1,400&family=Roboto:wght@500;700&display=swap" rel="stylesheet">
<style>
:root{
  --red:#d0282e;
  --red-dark:#b81f25;
  --navy:#233a6b;
  --navy-deep:#1c2f58;
  --ink:#222;
  --muted:#555;
  --white:#fff;
  --line:#e3e3e3;
}
*{margin:0;padding:0;box-sizing:border-box}
html,body{width:1200px;height:4967px;overflow:hidden}
body{position:relative;font-family:"Poppins",sans-serif;color:var(--ink);background:var(--white)}
.abs{position:absolute}
.heading{font-family:"Roboto",sans-serif;font-weight:500}
.btn{position:absolute;display:flex;align-items:center;justify-content:center;background:var(--red);color:var(--white);font-weight:600;border-radius:40px;text-transform:uppercase;font-family:"Poppins",sans-serif}

/* header */
.site-header{left:0;top:0;width:1200px;height:106px;background:var(--white);z-index:3}
.brand{left:70px;top:22px;display:flex;align-items:center;gap:12px;z-index:4}
.brand-mark{width:22px;height:22px;background:var(--red)}
.brand-name{font-family:"Roboto",sans-serif;font-weight:700;font-size:22px;line-height:1.05;color:var(--navy);text-transform:uppercase}
.main-nav{left:546px;top:33px;width:588px;height:46px;border:2px solid var(--navy);border-radius:30px;display:flex;align-items:center;padding:0 14px;justify-content:space-between}
.main-nav a{font-size:13px;color:var(--ink);text-decoration:none;font-weight:500;padding:7px 14px;border-radius:20px}
.main-nav a.active{background:var(--red);color:var(--white);font-weight:600}

/* hero */
.hero{left:0;top:106px;width:1200px;height:733px;background:linear-gradient(90deg,#2b4475 0%,#4b6187 35%,#b7a996 65%,#d9d2c6 85%,#8f9ab0 100%)}
.hero-title{left:68px;top:256px;font-family:"Roboto",sans-serif;font-weight:700;font-size:78px;line-height:87px;color:var(--white);text-transform:uppercase}
.hero .btn{}

/* about */
.ring{position:absolute;border:2px solid var(--red);border-radius:50%}
.ring .photo{position:absolute;border-radius:50%}
.eyebrow{position:absolute;color:var(--red);font-size:22px;letter-spacing:1px;text-transform:uppercase;font-weight:500}
.section-title{position:absolute;font-family:"Roboto",sans-serif;font-weight:500;color:var(--navy)}
.about-copy{left:612px;top:1150px;width:525px;font-size:13.5px;line-height:27px;color:var(--muted)}
.about-copy p{margin-bottom:18px}
.about-copy .lead{color:var(--ink);font-weight:600;font-size:14.5px}

/* services */
.services-band{left:0;top:1622px;width:1200px;height:475px;background:var(--red)}
.service{position:absolute;top:1923px;width:336px;text-align:center}
.service .disc{width:336px;height:336px;border-radius:50%;border:8px solid var(--white);box-shadow:0 0 0 2px var(--red)}
.service h3{font-family:"Roboto",sans-serif;font-weight:500;font-size:27px;color:var(--ink);margin-top:33px}
.arrow{position:absolute;width:58px;height:54px;border-radius:50%;display:flex;align-items:center;justify-content:center}
.arrow.prev{border:2px solid var(--red);background:var(--white)}
.arrow.next{background:var(--red)}

/* testimonials */
.review{position:absolute;top:2674px;width:322px;height:252px;background:var(--white);box-shadow:0 2px 10px rgba(0,0,0,.14);padding:34px 26px 0 26px}
.review p{font-style:italic;font-size:13.5px;line-height:24px;color:#444}
.reviewer{display:flex;align-items:center;gap:14px;margin-top:16px;position:relative}
.avatar{width:62px;height:62px;border-radius:50%;background:linear-gradient(135deg,#c9a48a,#6b4e3d)}
.reviewer .name{color:var(--red);font-weight:500;font-size:17px}
.stars{color:#f2b300;font-size:12px;letter-spacing:1px}
.quote{position:absolute;right:0;top:2px;font-family:"Roboto",sans-serif;font-weight:700;font-size:84px;line-height:1;color:var(--navy);height:44px;overflow:hidden}

/* cta */
.cta{left:0;top:3171px;width:1200px;height:685px;background:linear-gradient(180deg,#8d7b6b 0%,#b9aa98 30%,#9a8e84 52%,#3c4f78 72%,#233a6b 100%)}
.cta-title{left:0;top:3494px;width:1200px;text-align:center;font-family:"Roboto",sans-serif;font-weight:500;font-size:82px;line-height:92px;color:var(--white)}

/* contact */
.field{position:absolute;border:1px solid var(--line);box-shadow:0 1px 4px rgba(0,0,0,.08);background:var(--white);font-size:12px;color:#999;padding:14px 18px}

/* footer */
.site-footer{left:0;top:4560px;width:1200px;height:340px;background:var(--red);color:var(--white)}
.footer-brand{left:81px;top:4715px;display:flex;align-items:center;gap:12px}
.footer-brand .brand-mark{background:var(--white)}
.footer-brand .brand-name{color:var(--white);font-size:26px}
.foot-h{position:absolute;top:4652px;font-family:"Roboto",sans-serif;font-weight:500;font-size:21px;color:var(--white)}
.foot-h::after{content:"";display:block;width:30px;height:3px;background:var(--white);margin-top:8px}
.quick-links{left:343px;top:4716px;list-style:none;font-size:14px;line-height:26px}
.quick-links li::before{content:"";display:inline-block;width:9px;height:9px;border:2px solid var(--white);border-radius:50%;margin-right:10px;vertical-align:middle}
.contact-item{position:absolute;left:554px;display:flex;gap:14px;font-size:13.5px;line-height:17px;color:var(--white)}
.contact-item .ico{width:28px;height:28px;background:var(--navy);border:1px solid var(--white);display:flex;align-items:center;justify-content:center;flex:none}
.bottom-bar{left:0;top:4900px;width:1200px;height:67px;background:var(--navy-deep);color:var(--white);font-size:12px}
.social{position:absolute;top:4918px;width:28px;height:28px;border-radius:50%;background:var(--red);border:2px solid var(--white)}
</style>
</head>
<body>

<!-- Header -->
<header class="abs site-header"></header>
<div class="abs brand">
  <span class="brand-mark"></span>
  <span class="brand-name">Copperline<br>Ridge</span>
</div>
<nav class="abs main-nav">
  <a href="#" class="active">HOME</a>
  <a href="#">ABOUT US</a>
  <a href="#">SERVICES</a>
  <a href="#">TESTIMONIALS</a>
  <a href="#">CONTACT US</a>
</nav>

<!-- Hero -->
<section class="abs hero" role="img" aria-label="Small wooden model house on a desk with printed charts and a pen"></section>
<h1 class="abs hero-title">A true<br>Copperline<br>not just<br>a vendor.</h1>
<a class="btn" style="left:68px;top:612px;width:237px;height:69px;font-size:21px">Learn More</a>

<!-- About -->
<div class="ring" style="left:68px;top:978px;width:496px;height:496px">
  <div class="photo" style="left:30px;top:30px;width:432px;height:432px;background:linear-gradient(135deg,#8b8580,#cbc5bd 50%,#a59d93)" role="img" aria-label="Modern bathroom sink with black faucet and round mirror"></div>
</div>
<div class="eyebrow" style="left:614px;top:974px">Who We Are</div>
<h2 class="section-title" style="left:612px;top:1008px;font-size:49px;line-height:60px">About Our Property<br>Management Solutions</h2>
<div class="abs about-copy">
  <p class="lead">Our organization delivers comprehensive property management solutions that optimize asset performance and tenant satisfaction.</p>
  <p>By integrating advanced analytics with proven operational frameworks, our specialists ensure each property achieves sustained value appreciation.</p>
  <p>Drawing on decades of collective expertise, the team facilitates regulatory compliance, cost efficiency, and proactive maintenance. This disciplined approach enables owners to preserve capital, enhance occupancy rates, and demonstrate long-term resilience across diverse market conditions.</p>
</div>
<a class="btn" style="left:612px;top:1424px;width:191px;height:60px;font-size:18px">Read More</a>

<!-- Services -->
<section class="abs services-band"></section>
<div class="eyebrow" style="left:0;top:1716px;width:1200px;text-align:center;color:var(--white)">What We Do</div>
<h2 class="section-title" style="left:0;top:1740px;width:1200px;text-align:center;font-size:60px;color:var(--white)">Our Services</h2>
<p class="abs" style="left:100px;top:1832px;width:1000px;text-align:center;color:var(--white);font-size:13.5px;line-height:26px">Our analysis demonstrates that effective property oversight originates from meticulous operational planning, transparent communication channels, and data-driven performance metrics across every asset class.</p>

<div class="service" style="left:70px">
  <div class="disc" style="background:linear-gradient(135deg,#c9b69d,#e8e1d6 55%,#a8896a)" role="img" aria-label="Hands unfolding a paper on a wooden table"></div>
  <h3>Basic Service</h3>
</div>
<div class="service" style="left:436px">
  <div class="disc" style="background:linear-gradient(180deg,#d8d0c6,#c6bdb0 65%,#2e2a27)" role="img" aria-label="Minimal table lamp beside open books"></div>
  <h3>Intermediate Service</h3>
</div>
<div class="service" style="left:797px">
  <div class="disc" style="background:linear-gradient(135deg,#b9b1a6,#e6e1da 55%,#9e968c)" role="img" aria-label="Desk with lamp, vase of lilies and a person writing"></div>
  <h3>Advanced Service</h3>
</div>

<div class="arrow prev" style="left:536px;top:2365px"><svg width="14" height="14" viewBox="0 0 14 14"><path d="M9 2 4 7l5 5" fill="none" stroke="#d0282e" stroke-width="2.4"/></svg></div>
<div class="arrow next" style="left:606px;top:2365px"><svg width="14" height="14" viewBox="0 0 14 14"><path d="M5 2l5 5-5 5" fill="none" stroke="#fff" stroke-width="2.4"/></svg></div>

<!-- Testimonials -->
<div class="eyebrow" style="left:0;top:2542px;width:1200px;text-align:center">Client Reviews</div>
<h2 class="section-title" style="left:0;top:2568px;width:1200px;text-align:center;font-size:50px">Testimonials</h2>

<article class="review" style="left:83px">
  <p>Lorem ipsum dolor sit amet, consecte tur adipiscing elit. Pellentesque aliquet eros vitae placerat hendrerit. Maece nas maximus commodo sapien, vitae lobortis ligula</p>
  <div class="reviewer"><div class="avatar" role="img" aria-label="Client portrait"></div><div><div class="name">Marcus Hale</div><div class="stars">★★★★★</div></div><span class="quote">”</span></div>
</article>
<article class="review" style="left:440px">
  <p>Lorem ipsum dolor sit amet, consecte tur adipiscing elit. Pellentesque aliquet eros vitae placerat hendrerit. Maece nas maximus commodo sapien, vitae lobortis ligula</p>
  <div class="reviewer"><div class="avatar" role="img" aria-label="Client portrait"></div><div><div class="name">Marcus Hale</div><div class="stars">★★★★★</div></div><span class="quote">”</span></div>
</article>
<article class="review" style="left:795px">
  <p>Lorem ipsum dolor sit amet, consecte tur adipiscing elit. Pellentesque aliquet eros vitae placerat hendrerit. Maece nas maximus commodo sapien, vitae lobortis ligula</p>
  <div class="reviewer"><div class="avatar" style="background:linear-gradient(135deg,#e8c9a6,#a7744f)" role="img" aria-label="Client portrait"></div><div><div class="name">Elena Brooks</div><div class="stars">★★★★★</div></div><span class="quote">”</span></div>
</article>

<div class="arrow prev" style="left:536px;top:2984px"><svg width="14" height="14" viewBox="0 0 14 14"><path d="M9 2 4 7l5 5" fill="none" stroke="#d0282e" stroke-width="2.4"/></svg></div>
<div class="arrow next" style="left:606px;top:2984px"><svg width="14" height="14" viewBox="0 0 14 14"><path d="M5 2l5 5-5 5" fill="none" stroke="#fff" stroke-width="2.4"/></svg></div>

<!-- CTA -->
<section class="abs cta" role="img" aria-label="Architectural model of a modern single-storey house with warm interior light"></section>
<h2 class="abs cta-title">Submit Your Property<br>Management Inquiry</h2>
<a class="btn" style="left:475px;top:3708px;width:250px;height:67px;font-size:21px">Contact Us</a>

<!-- Contact -->
<div class="ring" style="left:85px;top:3960px;width:496px;height:496px">
  <div class="photo" style="left:30px;top:30px;width:432px;height:432px;background:radial-gradient(circle at 50% 45%,#d9c4a4,#a69a8e 60%,#857a70)" role="img" aria-label="Stack of wooden planks as building material"></div>
</div>
<div class="eyebrow" style="left:654px;top:3964px">Get In Touch</div>
<h2 class="section-title" style="left:651px;top:3982px;font-size:60px">Contact Us</h2>
<div class="field" style="left:654px;top:4086px;width:218px;height:48px">First Name:</div>
<div class="field" style="left:893px;top:4086px;width:220px;height:48px">Last Name:</div>
<div class="field" style="left:654px;top:4151px;width:218px;height:48px">Phone:</div>
<div class="field" style="left:893px;top:4151px;width:220px;height:48px">Email:</div>
<div class="field" style="left:654px;top:4219px;width:459px;height:141px">Message:</div>
<a class="btn" style="left:654px;top:4398px;width:181px;height:50px;font-size:17px">Submit Now</a>

<!-- Footer -->
<footer class="abs site-footer"></footer>
<div class="abs footer-brand"><span class="brand-mark"></span><span class="brand-name">Copperline<br>Ridge</span></div>

<h4 class="foot-h" style="left:343px">Quick Links</h4>
<ul class="abs quick-links" style="color:var(--white)">
  <li>About Us</li><li>Services</li><li>Testimonials</li><li>Contact Us</li>
</ul>

<h4 class="foot-h" style="left:554px">Contact Us</h4>
<div class="contact-item" style="top:4718px">
  <span class="ico"><svg width="14" height="14" viewBox="0 0 24 24"><path d="M6.6 10.8a15 15 0 0 0 6.6 6.6l2.2-2.2c.3-.3.7-.4 1-.2 1.1.4 2.3.6 3.6.6.6 0 1 .4 1 1V20c0 .6-.4 1-1 1A17 17 0 0 1 3 4c0-.6.4-1 1-1h3.5c.6 0 1 .4 1 1 0 1.3.2 2.5.6 3.6.1.3 0 .7-.2 1z" fill="#fff"/></svg></span>
  <span>CALL US<br>012 555 0147</span>
</div>
<div class="contact-item" style="top:4768px">
  <span class="ico"><svg width="14" height="12" viewBox="0 0 24 20"><rect x="1" y="2" width="22" height="16" fill="none" stroke="#fff" stroke-width="2"/><path d="M1 3l11 8 11-8" fill="none" stroke="#fff" stroke-width="2"/></svg></span>
  <span>EMAIL US<br>info@copperlineridgemanagement.com</span>
</div>
<div class="contact-item" style="top:4818px">
  <span class="ico"><svg width="12" height="15" viewBox="0 0 20 26"><path d="M10 1a8 8 0 0 0-8 8c0 6 8 16 8 16s8-10 8-16a8 8 0 0 0-8-8z" fill="#fff"/><circle cx="10" cy="9" r="3" fill="#233a6b"/></svg></span>
  <span>Address line Dummy here<br>Address line dummy</span>
</div>

<h4 class="foot-h" style="left:924px">Our Newsletter</h4>
<p class="abs" style="left:924px;top:4716px;width:200px;font-size:13px;line-height:17px;color:var(--white)">Subscribe our newsletter to get the latest news.</p>
<div class="abs" style="left:924px;top:4768px;width:195px;height:32px;background:var(--white)"></div>
<div class="abs" style="left:924px;top:4818px;width:98px;height:30px;background:var(--navy);border:1px solid var(--white);border-radius:6px;color:var(--white);font-size:10px;font-weight:600;display:flex;align-items:center;justify-content:center">SUBSCRIBE</div>

<div class="abs bottom-bar"><span class="abs" style="left:68px;top:26px">Copyright © 2026 All Rights Reserved By Company name</span></div>
<span class="social" style="left:1013px"></span>
<span class="social" style="left:1045px"></span>
<span class="social" style="left:1076px"></span>
<span class="social" style="left:1106px"></span>

</body>
</html>
```